Business Card Design for Brackfell Studios

Design the layout for a two-sided business card incorporating the logo design produced through Pixel Harbor by tomekdurish earlier this year. Design to be created as per specifications for standard size cards produced by Pryntle.com. Art work dimensions to be restricted to 3.66" x 2.16"

Front of card to include Brackfell Studios Logo and name and contact information. Back side to include logo only.

Target Market(s)

Photography clients.

Industry/Entity Type

Business

Contact Information for Business Card

Derek Hollis, Photographer
23-815 Osprey Hill Drive
Yellowknife, NT X0E 2K7

867-555-3182

derek@brackfellstudios.example

www.brackfellstudios.example

Font styles to use
Serif

Requirements
Must have
• Logo, name, contact information, email and website.
• Use colours from original logo design.
Nice to have
• I'm thinking a black background, but I'm open to other ideas.

```html
<!DOCTYPE html>
<html lang="en">
<head>
<meta charset="utf-8">
<title>Brackfell Studios – Business Card</title>
<link href="https://fonts.googleapis.com/css2?family=Cinzel:wght@400;500&family=Lato:wght@300;400&display=swap" rel="stylesheet">
<style>
  :root {
    --stage: #949599;
    --card-black: #060607;
    --gold: #d9b877;
    --gold-light: #ecd495;
    --teal: #1b8fa6;
    --teal-dark: #117a9a;
    --teal-light: #43adb9;
    --white: #ffffff;
  }
  html, body {
    margin: 0;
    width: 1200px;
    height: 1000px;
    overflow: hidden;
    background: var(--stage);
  }
  .card {
    position: absolute;
    left: 289px;
    width: 623px;
    height: 365px;
    background: var(--card-black);
    box-shadow: 4px 5px 8px rgba(0,0,0,0.35);
    overflow: hidden;
  }
  .card--front { top: 119px; }
  .card--back { top: 510px; }
  .card__art {
    position: absolute;
    inset: 0;
    width: 623px;
    height: 365px;
  }
  .brand {
    position: absolute;
    display: flex;
    align-items: center;
    gap: 12px;
  }
  .brand__mark {
    width: 70px;
    height: 70px;
    border-radius: 50%;
    border: 3px solid var(--white);
    box-sizing: border-box;
  }
  .brand__name {
    font-family: "Cinzel", serif;
    font-weight: 500;
    font-size: 23px;
    letter-spacing: 1px;
    color: var(--gold);
    line-height: 1;
  }
  .card--front .brand { left: 42px; top: 36px; }
  .card--back .brand { left: 172px; top: 142px; }
  .holder {
    position: absolute;
    left: 52px;
    top: 126px;
  }
  .holder__name {
    font-family: "Cinzel", serif;
    font-size: 32px;
    letter-spacing: 1px;
    line-height: 1;
    margin: 0;
    font-weight: 400;
  }
  .holder__first { color: var(--gold); }
  .holder__last { color: var(--teal); }
  .holder__role {
    font-family: "Lato", sans-serif;
    font-weight: 300;
    font-size: 20px;
    letter-spacing: 2px;
    color: var(--white);
    margin: 6px 0 0 1px;
  }
  .contact {
    position: absolute;
    left: 50px;
    top: 236px;
    margin: 0;
    padding: 0;
    list-style: none;
    font-family: "Lato", sans-serif;
    font-size: 12px;
    color: var(--white);
  }
  .contact__item {
    display: flex;
    align-items: flex-start;
    gap: 8px;
    height: 20px;
    line-height: 16px;
  }
  .contact__item--address { line-height: 13px; }
  .contact__icon {
    width: 16px;
    height: 16px;
    flex: none;
  }
</style>
</head>
<body>

<section class="card card--front" aria-label="Front of business card">
  <svg class="card__art" viewBox="0 0 623 365" aria-hidden="false">
    <defs>
      <radialGradient id="portraitTone" cx="0.55" cy="0.35" r="0.6">
        <stop offset="0" stop-color="#6a6a6a"/>
        <stop offset="0.55" stop-color="#3a3a3a"/>
        <stop offset="1" stop-color="#060607"/>
      </radialGradient>
      <linearGradient id="goldBand" x1="0" y1="0" x2="1" y2="0">
        <stop offset="0" stop-color="#c9a45e"/>
        <stop offset="1" stop-color="#ecd495"/>
      </linearGradient>
    </defs>
    <rect class="portrait" x="380" y="0" width="243" height="340" fill="url(#portraitTone)" role="img" aria-label="Black and white portrait photograph of the photographer"/>
    <path class="wave wave--gold" fill="url(#goldBand)" d="M0,206 C180,196 330,205 440,282 C520,330 570,334 623,333 L623,352 C560,354 520,347 440,302 C330,222 180,208 0,212 Z"/>
    <path class="wave wave--teal" fill="var(--teal)" d="M0,212 C180,208 330,222 440,302 C520,347 560,354 623,352 L623,365 L600,365 C540,362 500,354 440,318 C330,234 180,214 0,216 Z"/>
  </svg>

  <div class="brand">
    <span class="brand__mark"></span>
    <span class="brand__name">Brackfell Studios</span>
  </div>

  <div class="holder">
    <h1 class="holder__name"><span class="holder__first">Derek</span> <span class="holder__last">Hollis</span></h1>
    <p class="holder__role">Photographer</p>
  </div>

  <ul class="contact">
    <li class="contact__item">
      <svg class="contact__icon" viewBox="0 0 16 16"><circle cx="8" cy="8" r="8" fill="var(--teal)"/><path d="M5 11 L11 5" stroke="#fff" stroke-width="2" stroke-linecap="round"/></svg>
      <span>867-555-3182</span>
    </li>
    <li class="contact__item">
      <svg class="contact__icon" viewBox="0 0 16 16"><circle cx="8" cy="8" r="8" fill="var(--teal)"/><rect x="4" y="5.5" width="8" height="5.5" fill="#fff"/><path d="M4 5.5 L8 8.5 L12 5.5" stroke="var(--teal)" stroke-width="1" fill="none"/></svg>
      <span>derek@brackfellstudios.example</span>
    </li>
    <li class="contact__item">
      <svg class="contact__icon" viewBox="0 0 16 16"><circle cx="8" cy="8" r="8" fill="var(--teal)"/><circle cx="8" cy="8" r="4" fill="none" stroke="#fff" stroke-width="1.2"/><path d="M4 8 H12 M8 4 V12" stroke="#fff" stroke-width="0.8"/></svg>
      <span>www.brackfellstudios.example</span>
    </li>
    <li class="contact__item contact__item--address">
      <svg class="contact__icon" viewBox="0 0 16 16"><circle cx="8" cy="8" r="8" fill="var(--teal)"/><path d="M8 12.5 C6 10 5 8.5 5 7 A3 3 0 0 1 11 7 C11 8.5 10 10 8 12.5 Z" fill="#fff"/><circle cx="8" cy="7" r="1.1" fill="var(--teal)"/></svg>
      <span>23-815 Osprey Hill Drive<br>Yellowknife, NT X0E 2K7</span>
    </li>
  </ul>
</section>

<section class="card card--back" aria-label="Back of business card">
  <svg class="card__art" viewBox="0 0 623 365">
    <defs>
      <linearGradient id="tealTop" x1="0" y1="0" x2="0" y2="1">
        <stop offset="0" stop-color="#43adb9"/>
        <stop offset="1" stop-color="#117a9a"/>
      </linearGradient>
      <linearGradient id="tealBottom" x1="0" y1="0" x2="0" y2="1">
        <stop offset="0" stop-color="#117a9a"/>
        <stop offset="1" stop-color="#43adb9"/>
      </linearGradient>
    </defs>
    <path class="wave wave--teal" fill="url(#tealTop)" d="M95,0 L623,0 L623,122 C520,128 380,118 300,80 C220,40 170,0 95,0 Z"/>
    <path class="wave wave--gold" fill="var(--gold-light)" d="M0,0 L95,0 C170,0 220,40 300,80 C380,118 520,128 623,122 L623,127 C520,134 380,128 295,92 C210,50 150,6 0,5 Z"/>
    <path class="wave wave--teal" fill="url(#tealBottom)" d="M0,242 C120,232 250,235 340,270 C430,305 480,350 520,365 L0,365 Z"/>
    <path class="wave wave--gold" fill="var(--gold-light)" d="M0,236 C120,226 260,228 350,262 C450,300 520,345 623,360 L623,365 L520,365 C480,350 430,305 340,270 C250,235 120,232 0,242 Z"/>
  </svg>

  <div class="brand">
    <span class="brand__mark"></span>
    <span class="brand__name">Brackfell Studios</span>
  </div>
</section>

</body>
</html>
```